Poster Design Project

Poster with modern feeling to be displayed in office. The text that needs to be included in this poster is below:

Rules
1. If it’s not in writing it doesn’t exist.
2. No such thing as 'off the record.'
3. Do not hold a private conversation in a public place.
4. Don’t believe any number that ends in zero.
5. Never turn down an opportunity to eat or go to the bathroom.
6. Don’t spend any of your own money. Don’t even admit you own a credit card. Don’t spend money that is not yours.
7. Not always a 'right' or 'wrong' answer - 'It depends.'
8. In a campaign, someone has to be in charge – campaigns are a place to foster democracy, not practice it.
9. Assume nothing.
10. If you make a mistake, fix it before analyzing. Bad news doesn’t age well.

Industry/Entity Type

Credit Card

Requirements
Must have
• Rules
7. Not always a “right” or “wrong” answer - 'It depends.' 
9. Assume nothing.

```html
<!DOCTYPE html>
<html lang="en">
<head>
<meta charset="utf-8">
<title>Rules Poster</title>
<link href="https://fonts.googleapis.com/css2?family=Roboto+Condensed:wght@700&display=swap" rel="stylesheet">
<style>
  :root {
    --page-bg: #ffffff;
    --poster-edge: #2e3192;
    --poster-center: #0a52a8;
    --ink: #ffffff;
  }
  * { margin: 0; padding: 0; box-sizing: border-box; }
  html, body {
    width: 1200px;
    height: 900px;
    overflow: hidden;
    background: var(--page-bg);
  }
  .canvas {
    position: relative;
    width: 1200px;
    height: 900px;
  }
  .poster {
    position: absolute;
    left: 310px;
    top: 0;
    width: 580px;
    height: 900px;
    background: radial-gradient(ellipse 62% 48% at 50% 42%, var(--poster-center) 0%, #1747a0 45%, var(--poster-edge) 100%);
    font-family: "Roboto Condensed", "Arial Narrow", sans-serif;
    color: var(--ink);
  }
  .poster-title {
    position: absolute;
    top: 44px;
    left: 0;
    width: 100%;
    text-align: center;
    font-size: 64px;
    font-weight: 700;
    line-height: 80px;
    letter-spacing: -0.5px;
  }
  .title-rule {
    position: absolute;
    left: 60px;
    width: 459px;
    height: 3px;
    background: var(--ink);
  }
  .title-rule--upper { top: 127px; }
  .title-rule--lower { top: 135px; }
  .rule-list {
    position: absolute;
    top: 171px;
    left: 85px;
    width: 420px;
    list-style: none;
  }
  .rule-item {
    display: grid;
    grid-template-columns: 33px 1fr;
    column-gap: 10px;
    font-size: 20px;
    font-weight: 700;
    line-height: 27px;
    margin-bottom: 16px;
  }
  .rule-number { text-align: right; }
</style>
</head>
<body>
<div class="canvas">
  <section class="poster">
    <h1 class="poster-title">RULES</h1>
    <div class="title-rule title-rule--upper"></div>
    <div class="title-rule title-rule--lower"></div>
    <ol class="rule-list">
      <li class="rule-item"><span class="rule-number">1.</span><span class="rule-text">If it’s not in writing it doesn’t exist.</span></li>
      <li class="rule-item"><span class="rule-number">2.</span><span class="rule-text">No such thing as 'off the record.'</span></li>
      <li class="rule-item"><span class="rule-number">3.</span><span class="rule-text">Do not hold a private conversation in<br>a public place.</span></li>
      <li class="rule-item"><span class="rule-number">4.</span><span class="rule-text">Don’t believe any number that ends<br>in zero.</span></li>
      <li class="rule-item"><span class="rule-number">5.</span><span class="rule-text">Never turn down an opportunity to<br>eat or go to the bathroom.</span></li>
      <li class="rule-item"><span class="rule-number">6.</span><span class="rule-text">Don’t spend any of your own money.<br>Don’t even admit you own a credit card.<br>Don’t spend money that is not yours.</span></li>
      <li class="rule-item"><span class="rule-number">7.</span><span class="rule-text">Not always a 'right' or 'wrong'<br>answer - 'It depends.'</span></li>
      <li class="rule-item"><span class="rule-number">8.</span><span class="rule-text">In a campaign, someone has to be in<br>charge – campaigns are a place to<br>foster democracy, not practice it.</span></li>
      <li class="rule-item"><span class="rule-number">9.</span><span class="rule-text">Assume nothing.</span></li>
      <li class="rule-item"><span class="rule-number">10.</span><span class="rule-text">If you make a mistake, fix it before<br>analyzing. Bad news doesn’t age well.</span></li>
    </ol>
  </section>
</div>
</body>
</html>
```